Harbor Lantern Business Card
remarkable business card
Project: Harbor Lantern Business Card
Harbor Lantern Business Card - Events
Creative Brief
Use specific fonts
Use the fonts in my logo and/or the fonts that look best
Bright & Fun-filled
Tom Vesk
Culture Director
not to be listed on the card
Vesk@HarborLantern.example
www.HarborLantern.example
I want the Name to be prominent . I don't want the address to be listed This should be a very remarkable card. It needs to get instant attention that people will remember, and talk about. People should say wow! you need to see this card. That is a great looking card!

```html
<!DOCTYPE html>
<html lang="en">
<head>
<meta charset="utf-8">
<title>Harbor Lantern Business Card</title>
<link rel="stylesheet" href="https://fonts.googleapis.com/css2?family=Lato:wght@400&family=Tinos:wght@400;700&display=swap">
<style>
  :root {
    --backdrop: #ece8e3;
    --card-white: #ffffff;
    --card-fade: #e9e9e9;
    --green-light: #a6cf3c;
    --green-mid: #5fa83a;
    --green-dark: #1f7a3c;
    --brand-green: #3f9a34;
    --ink: #3c3c3c;
    --ink-soft: #6d6d6d;
    --swirl-warm: #f0a27c;
    --swirl-cool: #8fb6e0;
    --swirl-leaf: #b8d27a;
  }
  * { box-sizing: border-box; margin: 0; padding: 0; }
  html, body { width: 1200px; height: 761px; overflow: hidden; }
  body { background: var(--backdrop); position: relative; font-family: "Tinos", "Times New Roman", serif; }

  .card {
    position: absolute;
    border-radius: 14px;
    box-shadow: 0 6px 18px rgba(0,0,0,0.18);
    overflow: hidden;
  }

  /* Front card */
  .card--front {
    left: 100px; top: 150px; width: 550px; height: 330px;
    background: linear-gradient(180deg, var(--card-white) 0%, var(--card-white) 55%, var(--card-fade) 100%);
  }
  .brand { position: absolute; display: flex; align-items: center; gap: 16px; }
  .brand__dot { width: 58px; height: 58px; border-radius: 50%; background: var(--brand-green); }
  .brand__name { font-family: "Lato", Arial, sans-serif; font-weight: 400; color: var(--ink); font-size: 36px; line-height: 1; }
  .brand__tagline { font-family: "Tinos", serif; color: var(--brand-green); font-size: 15px; margin-top: 4px; }
  .card--front .brand { left: 30px; top: 40px; }

  .person { position: absolute; left: 40px; top: 150px; }
  .person__name { color: var(--brand-green); font-weight: 700; font-size: 30px; line-height: 1.05; }
  .person__title { color: var(--ink-soft); font-size: 17px; }

  .contact { position: absolute; left: 40px; font-size: 16px; color: var(--ink-soft); line-height: 1.35; }
  .contact--phones { top: 232px; }
  .contact--web { top: 282px; }

  /* Back card, green */
  .card--back {
    left: 662px; top: 48px; width: 490px; height: 330px;
    background: linear-gradient(90deg, var(--green-light) 0%, var(--green-mid) 55%, var(--green-dark) 100%);
  }
  .card--back .decor {
    position: absolute; left: 0; top: 0; width: 260px; height: 330px;
    background: radial-gradient(circle at 35% 50%, rgba(255,255,255,0.28), rgba(255,255,255,0) 70%);
  }
  .card--back .brand { right: 28px; bottom: 40px; display: block; text-align: left; }
  .card--back .brand__name { color: #ffffff; font-size: 34px; }
  .card--back .brand__tagline { color: #ffffff; font-size: 14px; }

  /* Second back, white */
  .card--alt {
    left: 403px; top: 389px; width: 566px; height: 331px;
    background: linear-gradient(180deg, var(--card-white) 0%, var(--card-fade) 100%);
  }
  .card--alt .decor {
    position: absolute; left: 0; top: 0; width: 300px; height: 331px;
    background:
      radial-gradient(circle at 20% 35%, rgba(240,162,124,0.35), rgba(240,162,124,0) 45%),
      radial-gradient(circle at 55% 75%, rgba(143,182,224,0.45), rgba(143,182,224,0) 45%),
      radial-gradient(circle at 60% 25%, rgba(184,210,122,0.4), rgba(184,210,122,0) 45%);
  }
  .card--alt .brand { right: 34px; bottom: 42px; display: block; }
  .card--alt .brand__name { font-size: 36px; }
</style>
</head>
<body>
  <section class="card card--front">
    <div class="brand">
      <span class="brand__dot"></span>
      <div>
        <div class="brand__name">Harbor Lantern</div>
        <div class="brand__tagline">Bringing the best to Families</div>
      </div>
    </div>
    <div class="person">
      <div class="person__name">Tom Vesk</div>
      <div class="person__title">Culture Director</div>
    </div>
    <div class="contact contact--phones">
      <div>Cell: 555-014-2290</div>
      <div>Fax: 555-018-7734</div>
    </div>
    <div class="contact contact--web">
      <div>Vesk@HarborLantern.example</div>
      <div>www.HarborLantern.example</div>
    </div>
  </section>

  <section class="card card--back">
    <div class="decor" role="img" aria-label="Faint decorative swirl motif on green"></div>
    <div class="brand">
      <div class="brand__name">Harbor Lantern</div>
      <div class="brand__tagline">Bringing the best to Families</div>
    </div>
  </section>

  <section class="card card--alt">
    <div class="decor" role="img" aria-label="Large soft multicolour swirl motif"></div>
    <div class="brand">
      <div class="brand__name">Harbor Lantern</div>
      <div class="brand__tagline">Bringing the best to Families</div>
    </div>
  </section>
</body>
</html>
```